Melbourne Gym Celebrating 49 years of business

We are celebrating our 49th birthday and will be running a "12 month Membership Special" $299.00 save over 30%. Being one of the longest running gyms in the fitness industry the design must be very eye catching and professional in its appearance. Given the length of operation, artwork must also have a touch of class that will appeal to 18-40 year old's. Below are previous specials with its layout and sample 49th Anniversary layouts. The final design should emphasis the advertised sale, along with celebrating 49 years. You can be as creative as possible with layout and design.

Target Market(s)

Male and females aged between 18-40

Font styles to use
Serif
Sans Serif

Requirements
Must have
• Must emphasize either "Celebrating 49 years" "49th Anniversary" or Happy 49th Birthday" and in a large font "12 Month Special $299.00 SAVE OVER 30%" Terms and Conditions Apply, Strictly Limited Time Only.
• "contact details"
• Address: 14 Harlow Rd Tindale Park
• Ph: 9517 2860
• www.corvalfitness.com.au
• Design format must come in poster size A0 size, Instagram format, Facebook cover and 800 x 800 for the website
Nice to have
• Given the number of years in business, an elegant/classy feel would be nice to the overall presentation. Bright colors can be used along with artistic graphic designs

```html
<!DOCTYPE html>
<html lang="en">
<head>
<meta charset="utf-8">
<title>Corval Fitness – 49th Anniversary Special</title>
<link rel="stylesheet" href="https://fonts.googleapis.com/css2?family=Montserrat:wght@500;600;700;800&family=Cinzel:wght@500&family=Great+Vibes&display=swap">
<style>
  :root {
    --bg-deep: #07090d;
    --bg-mid: #1d2836;
    --gold: #d8b45a;
    --gold-light: #f3dc94;
    --gold-dark: #8a6a22;
    --ink-dark: #14110b;
    --white: #ffffff;
    --skin: #6b4a35;
  }
  * { margin: 0; padding: 0; box-sizing: border-box; }
  html, body { width: 1199px; height: 1200px; overflow: hidden; background: var(--bg-deep); }
  .poster {
    position: relative;
    width: 1199px; height: 1200px;
    overflow: hidden;
    background: radial-gradient(ellipse 70% 60% at 50% 45%, var(--bg-mid) 0%, #111822 55%, var(--bg-deep) 100%);
    font-family: "Montserrat", sans-serif;
    color: var(--white);
  }
  .poster__frame {
    position: absolute; inset: 0;
    border: 6px solid var(--gold);
    pointer-events: none;
    z-index: 10;
  }
  .hero-photo {
    position: absolute;
    left: 260px; top: 470px;
    width: 920px; height: 730px;
    background:
      radial-gradient(ellipse 30% 42% at 48% 55%, rgba(150,100,70,0.85) 0%, rgba(107,74,53,0.55) 45%, rgba(107,74,53,0) 75%),
      radial-gradient(ellipse 50% 30% at 50% 40%, rgba(120,80,55,0.45) 0%, rgba(120,80,55,0) 80%);
  }
  .celebration {
    position: absolute;
    left: 142px; top: 40px; width: 520px;
    display: flex; align-items: center; gap: 10px;
    color: var(--gold);
  }
  .celebration__rule { flex: 1; height: 2px; background: var(--gold); }
  .celebration__word {
    font-family: "Great Vibes", cursive;
    font-size: 92px; line-height: 1;
    background: linear-gradient(180deg, var(--gold-light), var(--gold) 55%, var(--gold-dark));
    -webkit-background-clip: text; background-clip: text; color: transparent;
  }
  .anniversary-number { position: absolute; left: 120px; top: 100px; width: 600px; height: 540px; }
  .anniversary-label {
    position: absolute; left: 68px; top: 640px;
    font-family: "Cinzel", serif; font-weight: 500;
    font-size: 36px; letter-spacing: 17px;
    color: var(--gold-light);
  }
  .site-url {
    position: absolute; right: 48px; top: 58px;
    font-size: 29px; font-weight: 600; color: var(--gold);
  }
  .saving-box {
    position: absolute; left: 740px; top: 142px; width: 428px; height: 146px;
    background: linear-gradient(180deg, var(--gold-light), var(--gold));
    display: flex; align-items: center; justify-content: center; gap: 10px;
    color: var(--ink-dark);
  }
  .saving-box__lead { font-size: 50px; font-weight: 600; line-height: 0.95; }
  .saving-box__value { font-size: 104px; font-weight: 600; letter-spacing: -3px; line-height: 1; }
  .offer-title {
    position: absolute; left: 740px; top: 308px; width: 428px;
    text-align: center; font-weight: 600;
  }
  .offer-title__months { font-size: 60px; letter-spacing: 3px; line-height: 1.1; }
  .offer-title__special { font-size: 58px; letter-spacing: 13px; line-height: 1.05; }
  .offer-rule { position: absolute; left: 765px; top: 450px; width: 375px; height: 3px; background: var(--gold); }
  .offer-price {
    position: absolute; left: 740px; top: 462px; width: 428px;
    text-align: center; font-size: 96px; font-weight: 600; color: var(--gold);
  }
  .contact { position: absolute; left: 50px; top: 1038px; }
  .contact__row { display: flex; align-items: center; gap: 18px; font-size: 30px; font-weight: 600; height: 48px; margin-bottom: 8px; }
  .contact__row--phone { font-size: 38px; }
  .contact__icon { width: 30px; height: 34px; fill: var(--gold); flex: none; }
  .brand-name {
    position: absolute; left: 850px; top: 1030px; width: 290px;
    display: flex; flex-direction: column; align-items: center;
    font-family: "Montserrat", sans-serif; font-weight: 800; color: var(--white);
  }
  .brand-name__main { font-size: 66px; line-height: 1; letter-spacing: 1px; }
  .brand-name__sub { font-size: 30px; letter-spacing: 12px; line-height: 1.4; }
  .terms { position: absolute; left: 26px; top: 1160px; font-size: 15px; font-weight: 500; color: #d8d8d8; }
</style>
</head>
<body>
<main class="poster">
  <div class="hero-photo" role="img" aria-label="Muscular man in a cap posing with both arms raised, lit in warm light"></div>

  <div class="celebration">
    <span class="celebration__rule"></span>
    <span class="celebration__word">Celebration</span>
    <span class="celebration__rule"></span>
  </div>

  <svg class="anniversary-number" viewBox="0 0 600 540" aria-label="49th">
    <defs>
      <linearGradient id="goldFace" x1="0" y1="0" x2="0" y2="1">
        <stop offset="0" stop-color="#f6e3a2"/>
        <stop offset="0.45" stop-color="#d8b45a"/>
        <stop offset="1" stop-color="#9b7a2c"/>
      </linearGradient>
      <linearGradient id="goldSide" x1="0" y1="0" x2="1" y2="1">
        <stop offset="0" stop-color="#6e521a"/>
        <stop offset="1" stop-color="#b08a36"/>
      </linearGradient>
    </defs>
    <g font-family="Montserrat, sans-serif" font-weight="800" font-size="700">
      <text x="34" y="510" textLength="430" lengthAdjust="spacingAndGlyphs" fill="url(#goldSide)">49</text>
      <text x="30" y="506" textLength="430" lengthAdjust="spacingAndGlyphs" fill="url(#goldSide)">49</text>
      <text x="26" y="502" textLength="430" lengthAdjust="spacingAndGlyphs" fill="url(#goldSide)">49</text>
      <text x="22" y="498" textLength="430" lengthAdjust="spacingAndGlyphs" fill="url(#goldSide)">49</text>
      <text x="18" y="494" textLength="430" lengthAdjust="spacingAndGlyphs" fill="url(#goldFace)">49</text>
    </g>
    <text x="462" y="122" font-family="Montserrat, sans-serif" font-weight="800" font-size="88" fill="url(#goldFace)">th</text>
  </svg>

  <p class="anniversary-label">ANNIVERSARY</p>

  <p class="site-url">www.corvalfitness.com.au</p>

  <div class="saving-box">
    <span class="saving-box__lead">SAVE<br>OVER</span>
    <span class="saving-box__value">30%</span>
  </div>

  <div class="offer-title">
    <p class="offer-title__months">12 MONTHS</p>
    <p class="offer-title__special">SPECIAL</p>
  </div>
  <div class="offer-rule"></div>
  <p class="offer-price">$299.00</p>

  <div class="contact">
    <p class="contact__row">
      <svg class="contact__icon" viewBox="0 0 24 28" aria-hidden="true"><path d="M12 0C5.9 0 1 4.8 1 10.8 1 18.6 12 28 12 28s11-9.4 11-17.2C23 4.8 18.1 0 12 0zm0 15.2a4.4 4.4 0 1 1 0-8.8 4.4 4.4 0 0 1 0 8.8z"/></svg>
      14 Harlow Rd Tindale Park
    </p>
    <p class="contact__row contact__row--phone">
      <svg class="contact__icon" viewBox="0 0 24 24" aria-hidden="true"><path d="M6.6 10.8a15.2 15.2 0 0 0 6.6 6.6l2.2-2.2c.3-.3.7-.4 1-.2 1.1.4 2.3.6 3.6.6.6 0 1 .4 1 1V20c0 .6-.4 1-1 1A17 17 0 0 1 3 4c0-.6.4-1 1-1h3.5c.6 0 1 .4 1 1 0 1.3.2 2.5.6 3.6.1.3 0 .7-.2 1z"/></svg>
      9517 2860
    </p>
  </div>

  <div class="brand-name">
    <span class="brand-name__main">CORVAL</span>
    <span class="brand-name__sub">FITNESS</span>
  </div>

  <p class="terms">*terms and condition apply</p>

  <div class="poster__frame"></div>
</main>
</body>
</html>
```